"Dario Quillon" Business Card

Friends

My name is "Dario Quillon" and I need your help! I need a new business card for my personal use.

As background, "Dario Quillon" is actually an alias that I use when I meet women. Please use your creative skills to create an amazing business card for me to use!

In addition to including my name and contact details (see the "Must Have" section), you may wish to add a catchphrase or a title if you think it would help me :)

For background, please see:

http://www.dailybrightwire.com/2013/07/23/morton-feld-dario-quillon_n_5129847.html

Looking forward to seeing what you can do for me.

Hugs and kisses,

Dario Quillon [courtesy of PixelHarbor]

Target Market(s)

Adult women in New York City...or anywhere really.

Industry/Entity Type

Business

Requirements
Must have
• Please include the following details:

Dario Quillon
P: +1-555-3QUILLN
E: secrets@darioquillon-mail.com
Nice to have
• You might include a catchphrase, like "Quillon is my surname But you can call me Mr Smoothstep".

Or perhaps a title, like "Dario Quillon, Head of Sexy Times".

You're creative...I will leave the details to you my friends.
Should not have
• Any references to my actual name...because then, what's the point in using an alias?

```html
<!DOCTYPE html>
<html lang="en">
<head>
<meta charset="utf-8">
<title>Dario Quillon — Business Card</title>
<link rel="stylesheet" href="https://fonts.googleapis.com/css2?family=Nunito+Sans:wght@800&family=Advent+Pro:wght@200&family=Stardos+Stencil:wght@700&family=Quicksand:wght@300&display=swap">
<style>
  :root {
    --page: #ffffff;
    --panel-wine: #7b4b4e;
    --panel-wine-light: #8e6063;
    --panel-slate: #8a8a8a;
    --panel-slate-light: #9d9d9d;
    --name-white: #ffffff;
    --name-red: #e8202a;
    --title-white: #f4f4f4;
    --title-shadow: #6a6a6a;
    --email-ink: #1e1e1e;
  }
  html, body {
    margin: 0;
    padding: 0;
    width: 1200px;
    height: 713px;
    overflow: hidden;
    background: var(--page);
  }
  .card {
    position: absolute;
    left: 12px;
    top: 0;
    width: 1163px;
    height: 704px;
    overflow: hidden;
  }
  .photo {
    position: absolute;
    top: 0;
    height: 100%;
  }
  .photo--studio {
    left: 0;
    width: 563px;
    background: linear-gradient(160deg, var(--panel-wine-light), var(--panel-wine));
  }
  .photo--portrait {
    left: 563px;
    width: 600px;
    background: linear-gradient(200deg, var(--panel-slate-light), var(--panel-slate));
  }
  .card-text {
    position: absolute;
    inset: 0;
    width: 100%;
    height: 100%;
  }
  .name {
    font-family: "Nunito Sans", sans-serif;
    font-weight: 800;
    font-size: 176px;
    filter: drop-shadow(4px 6px 5px rgba(0,0,0,0.45));
  }
  .name__first { fill: var(--name-white); }
  .name__last { fill: var(--name-red); }
  .phone {
    font-family: "Advent Pro", sans-serif;
    font-weight: 200;
    font-size: 112px;
    fill: var(--name-white);
  }
  .email {
    font-family: "Quicksand", sans-serif;
    font-weight: 300;
    font-size: 74px;
    fill: var(--email-ink);
  }
  .title {
    font-family: "Stardos Stencil", serif;
    font-weight: 700;
    font-size: 50px;
    fill: var(--title-white);
    paint-order: stroke;
    stroke: var(--title-white);
    stroke-width: 1px;
  }
  .title-shadow {
    font-family: "Stardos Stencil", serif;
    font-weight: 700;
    font-size: 50px;
    fill: var(--title-shadow);
  }
</style>
</head>
<body>
  <div class="card">
    <div class="photo photo--studio" role="img" aria-label="Wine-tinted photo of a recording studio with a microphone stand"></div>
    <div class="photo photo--portrait" role="img" aria-label="Grey-tinted photo of a man standing in a studio"></div>

    <svg class="card-text" viewBox="0 0 1163 704" xmlns="http://www.w3.org/2000/svg">
      <text class="name" x="58" y="212" textLength="1040" lengthAdjust="spacingAndGlyphs"><tspan class="name__first">Dario</tspan> <tspan class="name__last">Quillon</tspan></text>

      <text class="phone" x="100" y="343" textLength="835" lengthAdjust="spacingAndGlyphs">+1-555-3 QUILLN</text>

      <g transform="translate(118 553) rotate(-10.5)">
        <text class="title-shadow" x="5" y="6" textLength="910" lengthAdjust="spacingAndGlyphs">DARIO QUILLON, HEAD OF SEXY TIMES</text>
        <text class="title" x="0" y="0" textLength="910" lengthAdjust="spacingAndGlyphs">DARIO QUILLON, HEAD OF SEXY TIMES</text>
      </g>

      <text class="email" x="126" y="630" textLength="915" lengthAdjust="spacingAndGlyphs">secrets@darioquillon-mail.com</text>
    </svg>
  </div>
</body>
</html>
```